MARVELTRUST web-presence redisign

We would like to have our existing web-presence redesigned. Have a look at www.pelbrika-example.ch (please use explorer). To the existing 11 pages we would add one more.

```html
<!DOCTYPE html>
<html lang="de">
<head>
<meta charset="utf-8">
<title>LUMADENT Zahnarztpraxis</title>
<link href="https://fonts.googleapis.com/css2?family=Open+Sans:wght@400;600;700&family=Arimo:wght@400&display=swap" rel="stylesheet">
<style>
:root{
  --navy:#1c1a4e;
  --heading:#0e0b3d;
  --plum:#7a1f5c;
  --nav-top:#f8f294;
  --nav-bottom:#efe674;
  --nav-line:#d9d27a;
  --panel:#4a7aa0;
  --panel-dark:#3e6b90;
  --badge:#f4ec7a;
  --accent:#f6e96b;
  --text:#3b3b3b;
  --rule:#d6d6d6;
  --footer:#222222;
  --footer-text:#9a9a9a;
}
*{margin:0;padding:0;box-sizing:border-box}
html,body{width:1200px;height:1147px;overflow:hidden;background:#fff}
body{position:relative;font-family:'Open Sans',sans-serif}
.brand{position:absolute;left:71px;top:48px;font-family:'Open Sans',sans-serif;font-weight:400;font-size:40px;letter-spacing:1px;color:var(--navy)}
.contact{position:absolute;left:976px;top:41px;display:flex;align-items:center;gap:10px}
.contact-lines{font-weight:700;font-size:15px;line-height:19px;color:var(--plum)}
.nav{position:absolute;left:47px;top:146px;width:1106px;height:41px;background:linear-gradient(var(--nav-top),var(--nav-bottom));border-bottom:1px solid #cfc76a;display:flex;box-shadow:0 2px 2px rgba(0,0,0,.12)}
.nav a{display:block;height:41px;line-height:41px;padding:0 20px 0 24px;font-weight:700;font-size:15px;color:var(--navy);text-decoration:none;border-right:1px solid var(--nav-line)}
.nav a:first-child{padding-left:25px;width:89px}
.hero{position:absolute;left:47px;top:187px;width:1106px;height:260px}
.hero svg{position:absolute;left:0;top:0}
.hero-text{position:absolute;left:720px;top:26px;width:360px;color:#fff}
.hero-text h2{font-size:15px;font-weight:700;margin-bottom:12px}
.hero-text p{font-size:14px;line-height:20px;height:60px;overflow:hidden}
.hero-text .more{display:block;margin-top:10px;font-size:14px;font-weight:700;color:var(--accent);text-decoration:none}
.badge{position:absolute;left:825px;top:340px;width:306px;height:106px;border-radius:50%;background:radial-gradient(ellipse at 50% 35%,#fbf6a6,var(--badge) 60%,#d9cf5c);box-shadow:2px 3px 4px rgba(0,0,0,.3);display:flex;align-items:center;justify-content:center;text-align:center;font-weight:700;font-size:15px;line-height:18px;color:var(--heading)}
.rule{position:absolute;left:47px;top:459px;width:1106px;height:1px;background:var(--rule)}
.portrait{position:absolute;left:47px;top:507px;width:177px;height:259px;background:linear-gradient(#cfeef4,#8fd0df);box-shadow:1px 1px 3px rgba(0,0,0,.3)}
.section-title{position:absolute;font-size:14px;font-weight:700;color:var(--heading);padding-bottom:2px;border-bottom:1px solid #9a9ab0}
.welcome-title{left:249px;top:505px}
.map-title{left:728px;top:505px}
.welcome{position:absolute;left:249px;top:540px;width:410px;font-family:'Arimo',sans-serif;font-size:15px;line-height:23.5px;color:var(--text)}
.welcome p{margin-bottom:11px}
.map{position:absolute;left:729px;top:547px;width:424px;height:218px;background:linear-gradient(135deg,#ece8df,#e2ddd2);box-shadow:1px 1px 3px rgba(0,0,0,.3)}
.footer{position:absolute;left:0;top:1054px;width:1200px;height:93px;background:var(--footer);border-top:2px solid #333}
.footer span{position:absolute;top:14px;font-family:'Arimo',sans-serif;font-size:12.5px;color:var(--footer-text)}
.footer .copy{left:35px}
.footer .rights{right:35px}
</style>
</head>
<body>
<div class="brand">LUMADENT</div>

<div class="contact">
  <svg width="36" height="66" viewBox="0 0 36 66" aria-hidden="true">
    <rect x="6" y="0" width="3" height="12" rx="1" fill="#8aa23a"/>
    <rect x="1" y="9" width="34" height="56" rx="7" fill="#8aa23a"/>
    <rect x="7" y="16" width="22" height="15" rx="3" fill="#e6efc4"/>
    <g fill="#e6efc4">
      <circle cx="11" cy="39" r="2"/><circle cx="18" cy="39" r="2"/><circle cx="25" cy="39" r="2"/>
      <circle cx="11" cy="46" r="2"/><circle cx="18" cy="46" r="2"/><circle cx="25" cy="46" r="2"/>
      <circle cx="11" cy="53" r="2"/><circle cx="18" cy="53" r="2"/><circle cx="25" cy="53" r="2"/>
    </g>
  </svg>
  <div class="contact-lines">+41 (0)44 555 01 23<br>info@lumadent-example.ch</div>
</div>

<nav class="nav">
  <a href="#">Home</a>
  <a href="#">Zahnmedizin</a>
  <a href="#">Dentalhygiene</a>
  <a href="#">Team</a>
  <a href="#">Kontakt</a>
</nav>

<section class="hero">
  <svg width="1106" height="260" viewBox="0 0 1106 260">
    <defs>
      <linearGradient id="photoTone" x1="0" y1="0" x2="1" y2="1">
        <stop offset="0" stop-color="#d8b8a2"/>
        <stop offset=".5" stop-color="#e6c7b0"/>
        <stop offset="1" stop-color="#a9c3da"/>
      </linearGradient>
    </defs>
    <path d="M0 0H682V232Q340 284 0 224Z" fill="url(#photoTone)" role="img" aria-label="Foto: lächelndes Paar mit gesunden Zähnen"/>
    <path d="M682 0H1106V140Q900 212 682 234Z" fill="var(--panel)"/>
  </svg>
  <div class="hero-text">
    <h2>DENTALHYGIENE</h2>
    <p>Zur modernen Zahmedizin gehört die Dentalhygiene, welche den Erhalt der eigenen Zähne verlängert. Kombiniert mit einer guten Mundhygiene, ermöglicht</p>
    <a class="more" href="#">Mehr lesen &gt;&gt;</a>
  </div>
</section>

<div class="badge">LUMADENT Zahnarztpraxis<br>Dr. med. dent. Clara Weiss-Imhof<br>Lindenweg 12<br>CH-8600 Musterdorf</div>

<div class="rule"></div>

<div class="portrait" role="img" aria-label="Porträtfoto der Zahnärztin"></div>

<h3 class="section-title welcome-title">HERZLICH WILLKOMMEN IN UNSERER NEUEN PRAXIS</h3>
<div class="welcome">
  <p>Es ist unser Ziel, Ihr Wohlbefinden zu steigern. Sie sollen die Schönheit des Alltags mit gesunden Zähnen geniessen und in jeder Situation herzhaft lachen können.</p>
  <p>Ihre Zahnärztin</p>
  <p>Dr. med. dent. Clara Weiss-Imhof</p>
</div>

<h3 class="section-title map-title">FINDEN SIE UNS AUF DER KARTE</h3>
<div class="map" role="img" aria-label="Stadtplan mit dem Standort der Praxis"></div>

<footer class="footer">
  <span class="copy">Copyright 2014 © LUMADENT | Dr. med. dent. C. Weiss-Imhof</span>
  <span class="rights">All rights reserved. Privacy Policy</span>
</footer>
</body>
</html>
```